Venmora Crest Holdings Limited is a asset management company and project funding company, we specialise in high end finance for high net worth individuals, we are looking for a new logo letterhead template, email footer template and business card design. The letterhead template should be designed in word format so that the letterheading can be used electronically.

Below is the current logo that is a but plain and a little cheaper looking, colour schemes are not important just that it looks professional.

I am looking for a sharp impact that stands out,

Target Market(s)

High net worth individuals and institutions

Industry/Entity Type

Finance

Contact Information for Business Card

Venmora Crest Holdings Limited
T: 0333 418 2965

M: 07531 492718
E:derek.holt@venmora-cresthold.example

MARLOW QUAY, EAST CORAL ROAD
SECOND FLOOR, SUITE 210
P.O. BOX FX-47315
NASSAU BAHAMAS

Logo Text

Font styles to use
Serif
Sans Serif
Script
Other font styles liked:
• Tahoma

Colors
fbed22
6b449b
ec1f27
f78f20
33b8a4
0592cd

Requirements
Must have
• Colours schemes would look good in blue’s green’s purples.

Yellow and Purple together maybe a nice combination.
Nice to have
• I want the log to look sharpe, relate to a global presence, but I also want to it to look established.
Should not have
• N/a

```html
<!DOCTYPE html>
<html lang="en">
<head>
<meta charset="utf-8">
<title>Venmora Crest Holdings Limited – Business Card</title>
<link href="https://fonts.googleapis.com/css2?family=Roboto:wght@400;500;700&display=swap" rel="stylesheet">
<style>
  :root {
    --teal: #1a9ea6;
    --teal-deep: #14888f;
    --orange: #f7a21e;
    --ink: #4b4b4b;
    --paper: #ffffff;
    --backdrop: #ece8e2;
  }
  * { margin: 0; padding: 0; box-sizing: border-box; }
  html, body {
    width: 1071px; height: 1200px; overflow: hidden;
    background: var(--backdrop);
    font-family: "Roboto", Arial, sans-serif;
  }
  .canvas { position: relative; width: 1071px; height: 1200px; }

  .card {
    position: absolute; left: 204px; width: 696px; height: 386px;
    background: var(--paper);
    box-shadow: 0 14px 22px rgba(0,0,0,0.22);
  }
  .card--front { top: 159px; }
  .card--back { top: 627px; }

  /* front: contact block */
  .holder { position: absolute; left: 53px; top: 95px; }
  .holder__name { color: var(--teal); font-weight: 700; font-size: 21px; line-height: 25px; letter-spacing: 0.2px; }
  .holder__role { color: var(--orange); font-weight: 500; font-size: 19px; line-height: 24px; }

  .address { position: absolute; left: 53px; top: 155px; color: var(--ink); font-size: 18.5px; line-height: 23.3px; }

  .contacts { position: absolute; left: 53px; top: 255px; color: var(--ink); font-size: 18.5px; }
  .contacts__item { display: flex; align-items: center; height: 23.5px; }
  .contacts__icon { width: 17px; height: 20px; margin-right: 7px; flex: none; }

  .web-band {
    position: absolute; left: 0; top: 336px; width: 696px; height: 31px;
    background: linear-gradient(to right, var(--teal) 0 667px, var(--orange) 667px);
  }
  .web-band__url {
    position: absolute; left: 53px; top: 5px;
    color: #fff; font-size: 17px; letter-spacing: 7.4px; line-height: 21px;
  }
  .web-band__dot {
    position: absolute; left: 617px; top: -11px; width: 52px; height: 52px;
    border-radius: 50%; background: #fff;
  }

  /* brand lockup */
  .brand { position: absolute; text-align: center; color: var(--teal-deep); font-weight: 700; }
  .brand__dot { border-radius: 50%; background: var(--teal); margin: 0 auto; }
  .brand__name { display: block; white-space: nowrap; }

  .brand--front { left: 384px; top: 50px; width: 280px; }
  .brand--front .brand__dot { width: 76px; height: 76px; margin-bottom: 16px; }
  .brand--front .brand__name--main { font-size: 25px; letter-spacing: 4px; line-height: 28px; }
  .brand--front .brand__name--sub { font-size: 15px; letter-spacing: 4px; line-height: 20px; margin-top: 3px; }

  .brand--back { left: 98px; top: 85px; width: 500px; }
  .brand--back .brand__dot { width: 130px; height: 130px; margin-bottom: 26px; }
  .brand--back .brand__name--main { font-size: 37px; letter-spacing: 6px; line-height: 42px; }
  .brand--back .brand__name--sub { font-size: 25px; letter-spacing: 7px; line-height: 30px; margin-top: 6px; }
</style>
</head>
<body>
<div class="canvas">

  <section class="card card--front" aria-label="Business card front">
    <div class="holder">
      <p class="holder__name">MARCUS DELANE</p>
      <p class="holder__role">President &amp; CEO</p>
    </div>

    <address class="address" style="font-style:normal">
      MARLOW QUAY, EAST CORAL ROAD<br>
      SECOND FLOOR, SUITE 210<br>
      P.O. BOX FX-47315<br>
      NASSAU BAHAMAS
    </address>

    <ul class="contacts" style="list-style:none">
      <li class="contacts__item">
        <svg class="contacts__icon" viewBox="0 0 17 20" aria-hidden="true">
          <rect x="3" y="0.5" width="11" height="19" rx="2" fill="none" stroke="#1a9ea6" stroke-width="1.8"/>
          <rect x="5" y="3" width="7" height="11" fill="#1a9ea6"/>
          <circle cx="8.5" cy="16.5" r="1.1" fill="#1a9ea6"/>
        </svg>
        07531 492718
      </li>
      <li class="contacts__item">
        <svg class="contacts__icon" viewBox="0 0 17 20" aria-hidden="true">
          <path d="M1 8 Q8.5 2 16 8 L14 10 L11.5 8 L5.5 8 L3 10 Z" fill="#1a9ea6"/>
          <rect x="3" y="10" width="11" height="7" rx="1" fill="#1a9ea6"/>
          <circle cx="8.5" cy="13.5" r="2" fill="#fff"/>
        </svg>
        0333 418 2965
      </li>
      <li class="contacts__item">
        <svg class="contacts__icon" viewBox="0 0 17 20" aria-hidden="true">
          <rect x="0.5" y="5" width="16" height="11" fill="#1a9ea6"/>
          <path d="M0.5 5 L8.5 11.5 L16.5 5 M0.5 16 L6 10 M16.5 16 L11 10" fill="none" stroke="#fff" stroke-width="1.2"/>
        </svg>
        derek.holt@venmora-cresthold.example
      </li>
    </ul>

    <div class="brand brand--front">
      <div class="brand__dot" aria-hidden="true"></div>
      <span class="brand__name brand__name--main">VENMORA CREST</span>
      <span class="brand__name brand__name--sub">HOLDINGS LIMITED</span>
    </div>

    <div class="web-band">
      <span class="web-band__url">www.venmora-cresthold.example</span>
      <span class="web-band__dot" aria-hidden="true"></span>
    </div>
  </section>

  <section class="card card--back" aria-label="Business card back">
    <div class="brand brand--back">
      <div class="brand__dot" aria-hidden="true"></div>
      <span class="brand__name brand__name--main">VENMORA CREST</span>
      <span class="brand__name brand__name--sub">HOLDINGS LIMITED</span>
    </div>
  </section>

</div>
</body>
</html>
```